Coupon/promo code site

I am looking for a one page website that will provide a list of coupon codes that are used at checkout when buying something online. The site will only have coupon codes for one online retailer. I would like this to be generic (i.e. not specific to any one retailer). I would like to have some interchangeable parts so that I could later customize the site so that it is specific to any given retailer.

I envision the site having a list of coupon codes with information about each code like when it expires and what it provides. For example there would be a: code, expiration date, short description or name, and a longer description (i.e. details).
Updates

Project Deadline Extended
Reason: I am going to submit a wire frame that provides a better idea of what I am looking for.

I have uploaded a wire frame that gives a more clear indication of what I am looking for.  Please see this before submitting designs.  If you have already submitted a design, please revise your design considering the wire frame I have provided.

Thanks,
Derek

Target Market(s)

Someone who is shopping online and searching for a specific retailers coupon codes

Industry/Entity Type

Coupon

Requirements
Must have
• I would like the site to have a white or light colored background.

I need a place or two where I can interchangeably place different retailers' logos.

The web page should have a title like, "[retailer's] online coupon code"

In addition to a list or table of coupon codes, there should below this be a list or table of special offers or sale items.

At the very bottom in a way that is not too noticeable, it should say, "This coupon site was created by PLW Deals."

There should be a section (probably on the right side) that allows a user to submit their email address to be notified in the future of specials/deals for this retailer.

There should be a nice looking link that goes to the online retailer's website.
Nice to have
• Example sites with a look and feel that I like are:

http://www.trolvania.com/
https://thebrimlet.com/
http://www.pixelgrove.com

This is an example of a site with coupon codes for just one retailer. This site is a little too busy, but you get the idea:
www.makeaplank.com/coupon-codes‎

```html
<!DOCTYPE html>
<html lang="en">
<head>
<meta charset="utf-8">
<title>Company Name Promo Codes</title>
<link href="https://fonts.googleapis.com/css2?family=Fredoka:wght@600&family=Open+Sans:wght@300&family=Anton&family=Arimo:wght@400;700&display=swap" rel="stylesheet">
<style>
:root{
  --blue:#0a8fd2;
  --blue-dark:#0b6fa8;
  --red:#e41e22;
  --panel:#e4e4e4;
  --ink:#333;
  --muted:#666;
  --chip:#555;
  --white:#fff;
}
*{margin:0;padding:0;box-sizing:border-box}
html,body{width:850px;height:1200px;overflow:hidden;background:var(--white);font-family:Arimo,Arial,sans-serif;color:var(--ink)}
.page{position:relative;width:850px;height:1200px}
.site-header{position:absolute;left:0;top:0;width:850px;height:98px;border-bottom:1px dashed #ccc}
.brand{position:absolute;left:20px;top:30px;height:40px;display:flex;align-items:center;gap:10px}
.brand .dot{width:16px;height:16px;border-radius:50%;background:var(--red)}
.brand .name{font-family:Fredoka,sans-serif;font-weight:600;font-size:28px;color:var(--red)}
.page-title{position:absolute;left:244px;top:26px;font-family:Fredoka,sans-serif;font-weight:600;font-size:40px;color:var(--blue);letter-spacing:.8px;white-space:nowrap}
.intro{position:absolute;left:0;top:98px;width:850px;height:156px;border-bottom:1px dashed #ccc;text-align:center;font-family:"Open Sans",sans-serif;font-weight:300;font-size:37px;line-height:36px;letter-spacing:-1.6px;padding-top:22px;color:#222}
.panel{position:absolute;left:6px;width:599px;background:var(--panel);border-radius:10px}
.section-head{position:absolute;left:8px;right:8px;top:7px;height:34px;background:var(--blue);border-radius:6px;padding:0 12px;display:flex;align-items:center;font-family:Fredoka,sans-serif;font-weight:600;font-size:16.5px;color:var(--white);letter-spacing:.3px}
.section-head::after{content:"";position:absolute;inset:2px;border:1px dashed rgba(255,255,255,.8);border-radius:5px}
.coupon{position:absolute;left:9px;width:581px;height:104px;background:var(--white);border-radius:8px}
.coupon h3{position:absolute;left:15px;top:12px;font-weight:400;font-size:16.5px;color:#222;white-space:nowrap}
.coupon p{position:absolute;left:15px;top:35px;width:340px;font-size:10.5px;line-height:12px;color:#444}
.coupon .expires{position:absolute;left:15px;top:83px;font-size:11px;color:var(--red)}
.coupon .label{position:absolute;left:357px;top:12px;font-size:16px;color:#222;white-space:nowrap}
.coupon .code{position:absolute;left:472px;top:9px;width:102px;height:25px;background:var(--chip);border-radius:7px;color:var(--white);font-weight:700;font-size:12px;letter-spacing:1px;display:flex;align-items:center;justify-content:center}
.coupon .code.revealed{background:#8a8a8a}
.coupon .hint{position:absolute;left:476px;top:38px;font-size:9px;color:#444}
.coupon .shop{position:absolute;right:17px;top:80px;font-size:12.5px;color:#444;white-space:nowrap}
.coupon .shop a{color:#333;font-weight:700;text-decoration:none;margin-left:6px}
.tip{position:absolute;left:486px;top:286px;width:107px;height:34px;background:var(--red);border-radius:6px;color:var(--white);text-align:center;font-size:10px;line-height:11px;padding-top:6px;z-index:2}
.tip::after{content:"";position:absolute;left:46px;bottom:-7px;border:7px solid transparent;border-top-color:var(--red);border-bottom:0}
.cursor{position:absolute;left:556px;top:346px;z-index:3}
.side-box{position:absolute;left:622px;width:213px;background:var(--panel)}
.side-head{position:absolute;left:0;right:0;background:var(--blue);color:var(--white);font-family:Anton,sans-serif}
.side-head::after{content:"";position:absolute;left:0;right:0;top:3px;bottom:3px;border-top:1px dashed rgba(255,255,255,.8);border-bottom:1px dashed rgba(255,255,255,.8)}
.news-text{position:absolute;left:12px;right:12px;top:104px;text-align:center;font-size:10.5px;line-height:12.5px;color:#666}
.email{position:absolute;left:10px;top:166px;width:195px;height:21px;background:var(--white);border:1px solid #ccc;border-radius:4px;font-size:9.5px;color:#333;padding:4px 10px}
.subscribe{position:absolute;left:11px;top:198px;width:91px;height:26px;border-radius:3px;background:linear-gradient(#2aa7e6,var(--blue-dark));color:var(--white);font-family:Anton,sans-serif;font-size:15px;display:flex;align-items:center;justify-content:center}
.socials{position:absolute;left:0;right:0;top:66px;display:flex;justify-content:center;gap:8px}
.socials span{width:24px;height:24px;border-radius:50%;background:#777}
.site-footer{position:absolute;left:0;top:1113px;width:850px;height:72px;background:#e4e4e4;text-align:center;padding-top:21px}
.site-footer .copy{font-size:10.5px;color:#333}
.site-footer .credit{font-size:9.5px;color:#888;margin-top:6px}
</style>
</head>
<body>
<div class="page">
  <header class="site-header">
    <div class="brand"><span class="dot"></span><span class="name">Brightmart</span></div>
    <h1 class="page-title">Company Name PROMO CODES</h1>
  </header>

  <section class="intro">
    Welcome to the Company Name promo page.<br>
    Here you will find the best and most up to date<br>
    promo codes available directly form Company name
  </section>

  <section class="panel" style="top:266px;height:507px">
    <div class="section-head">Feature Promo Codes</div>
    <article class="coupon" style="top:52px">
      <h3>$51.26 Average savings on Brightmart.com</h3>
      <p>Receive up to 60% off + Extra 20% off Select Jewelry &amp; Watches.</p>
      <span class="expires">Offer Expires: Aug 24, 2013</span>
      <span class="label">Coupon Code:</span>
      <span class="code revealed">12FOR12</span>
      <span class="shop">Use this code when shopping at : <a href="#">Brightmart.com</a></span>
    </article>
    <article class="coupon" style="top:165px">
      <h3>Free Shipping</h3>
      <p>Receive free shipping on orders over $50. The description<br>could wrap like this</p>
      <span class="expires">Offer Expires: Aug 24, 2013</span>
      <span class="label">Coupon Code:</span>
      <span class="code"></span><span class="hint">hover and copy code</span>
      <span class="shop">Use this code when shopping at : <a href="#">Brightmart.com</a></span>
    </article>
    <article class="coupon" style="top:277px">
      <h3>$51.26 Average savings on Brightmart.com</h3>
      <p>Receive up to 60% off + Extra 20% off Select Jewelry &amp; Watches.</p>
      <span class="expires">Offer Expires: Aug 24, 2013</span>
      <span class="label">Coupon Code:</span>
      <span class="code"></span><span class="hint">hover and copy code</span>
      <span class="shop">Use this code when shopping at : <a href="#">Brightmart.com</a></span>
    </article>
    <article class="coupon" style="top:391px">
      <h3>Free Shipping</h3>
      <p>Receive free shipping on orders over $50. The description<br>could wrap like this</p>
      <span class="expires">Offer Expires: Aug 24, 2013</span>
      <span class="label">Coupon Code:</span>
      <span class="code"></span><span class="hint">hover and copy code</span>
      <span class="shop">Use this code when shopping at : <a href="#">Brightmart.com</a></span>
    </article>
  </section>

  <div class="tip">CLICK<br>to copy code</div>
  <svg class="cursor" width="22" height="24" viewBox="0 0 22 24" aria-hidden="true">
    <path d="M6 2v11l-2-2c-1-1-3 0-2 2l5 7c1 2 3 3 5 3h3c3 0 5-2 5-5v-6c0-1-2-1-2 0v-1c0-1-2-1-2 0v-1c0-1-2-1-2 0V2c0-1.5-3-1.5-3 0z" fill="#fff" stroke="#222" stroke-width="1.2"/>
  </svg>

  <section class="panel" style="top:804px;height:280px">
    <div class="section-head">Special Offers &amp; Sales Items</div>
    <article class="coupon" style="top:51px">
      <h3>$51.26 Average savings on Brightmart.com</h3>
      <p>Receive up to 60% off + Extra 20% off Select Jewelry &amp; Watches.</p>
      <span class="expires">Offer Expires: Aug 24, 2013</span>
      <span class="label">Coupon Code:</span>
      <span class="code"></span>
      <span class="shop">Use this code when shopping at : <a href="#">Brightmart.com</a></span>
    </article>
    <article class="coupon" style="top:165px">
      <h3>Free Shipping</h3>
      <p>Receive free shipping on orders over $50. The description<br>could wrap like this</p>
      <span class="expires">Offer Expires: Aug 24, 2013</span>
      <span class="label">Coupon Code:</span>
      <span class="code"></span><span class="hint">hover and copy code</span>
      <span class="shop">Use this code when shopping at : <a href="#">Brightmart.com</a></span>
    </article>
  </section>

  <aside class="side-box" style="top:266px;height:242px">
    <div class="side-head" style="top:6px;height:78px">
      <svg style="position:absolute;left:13px;top:12px" width="60" height="50" viewBox="0 0 60 50" aria-hidden="true">
        <path d="M2 20 30 2 58 20v28H2z" fill="#fff"/>
        <rect x="14" y="12" width="32" height="22" rx="2" fill="#0a8fd2" stroke="#fff" stroke-width="2"/>
        <path d="M22 19h16M22 23h16M22 27h16" stroke="#fff" stroke-width="2"/>
        <path d="M2 20l28 18 28-18" fill="none" stroke="#0a8fd2" stroke-width="2.5"/>
      </svg>
      <div style="position:absolute;left:82px;top:12px;font-size:23px;line-height:27px">Never Miss<br>Another Deal!</div>
    </div>
    <p class="news-text">Our promotions are updated frequently, so be sure to sign-up for our newsletter to receive notification of new promo codes and exclusive offers.</p>
    <div class="email">Enter Your Email Address Here</div>
    <div class="subscribe">subscribe</div>
  </aside>

  <aside class="side-box" style="top:519px;height:102px">
    <div class="side-head" style="top:6px;height:38px;display:flex;align-items:center;justify-content:center;font-size:23px">Our Socials</div>
    <div class="socials"><span></span><span></span><span></span><span></span><span></span></div>
  </aside>

  <footer class="site-footer">
    <div class="copy">Copyright © 2013 dealharbor.com All rights reserved.</div>
    <div class="credit">This coupon site was created by PLW Deals</div>
  </footer>
</div>
</body>
</html>
```